Harrow WordPress Design Contest

We need a wordpress design that will incorporate a professional color scheme with company logo in a clean layout. The design needs to consider that this will be developed on a responsive theme. Colors are up to the designer - The green of the logo with black, gray or an accent color. Client wants a 'modern' look.

Industry/Entity Type

It Company

Number of Pages Required

1 page

Font styles to use
Serif
Sans Serif

Requirements
Must have
• Navigation: 1) Home 2) All Auctions 3) Real Estate for Sale 4) Services 5) About Us 6) Contact Us
• Colors - a corporate look with professional color scheme. Green of logo + black and gray, or an eggshell/light beige, or any other accent that keeps within a corporate look.
• In header - logo (attached) , and contact info :5127 Old Tenbury Lane, Scottsville, KY 42190
• 270-555-0143
• Fax: 270-555-0179
• Email:info@harrowlandbidhouse.example
• Design will feature a full width (960 px) slideshow - use a stock photo for real estate.
• Widgets in sidebar or where appropriate - 1) Email Signup 2) Message of the Day 3) Upcoming Auctions 4) News&Events blog 5) Testimonials 6) Social media - QX, chirpo, vidloop, snapboard, zentro+
• Footer will have company logo, association logos (attached) and contact info, with another widget area if necessary
Nice to have
• use of drop down menu styling - Upcoming Auctions / Online Auctions/ Past Auctions under the "Auction Calendar" menu item

```html
<!DOCTYPE html>
<html lang="en">
<head>
<meta charset="utf-8">
<title>Harrow Real Estate &amp; Auction Co.</title>
<link rel="stylesheet" href="https://fonts.googleapis.com/css2?family=Ubuntu:ital,wght@0,400;0,500;0,700;1,400;1,500;1,700&family=Roboto+Condensed:wght@400;700&display=swap">
<style>
:root{
  --green:#0e6b3a;
  --green-dark:#0a5a30;
  --green-btn:#1f8a4c;
  --page:#d6d6d6;
  --white:#ffffff;
  --panel:#ececec;
  --panel-line:#d4d4d4;
  --ink:#1d1d1d;
  --nav-top:#4a4a55;
  --nav-bot:#1f1f27;
  --sky:#4ab0b8;
  --link-blue:#2a8fd0;
  --menu-blue:#2aa3de;
  --quote-bg:#6b6b6b;
  --footer-bg:#363636;
  --muted:#c8c8c8;
}
*{box-sizing:border-box;margin:0;padding:0}
html,body{width:1200px;height:2161px;overflow:hidden}
body{background:var(--page);font-family:"Ubuntu",sans-serif;color:var(--ink);position:relative}
.abs{position:absolute}
.site{position:absolute;left:79px;top:17px;width:1046px;height:2127px;background:var(--white)}

/* header */
.header{left:0;top:0;width:1046px;height:287px;background:var(--green)}
.brand{left:0;top:0;width:428px;height:278px;background:var(--white);border:6px solid var(--green);display:flex;align-items:center;justify-content:center;gap:16px}
.brand-mark{width:34px;height:34px;background:var(--green)}
.brand-name{font-weight:700;font-size:86px;color:var(--green);letter-spacing:1px}
.contact-list{left:615px;top:42px;list-style:none;color:var(--white);font-size:15px;font-weight:500}
.contact-list li{height:26px;display:flex;align-items:center;gap:6px}
.contact-list svg{width:14px;height:14px}
.find-us{left:572px;top:189px;display:flex;align-items:center;gap:8px;color:var(--white);font-size:19px;font-weight:500}
.find-us .tag{width:20px;height:18px;background:#dcdcdc;border-radius:3px}
.social{display:flex;gap:21px;list-style:none}
.social li{width:43px;height:43px;border-radius:50%;background:var(--white);display:flex;align-items:center;justify-content:center;font-weight:700;font-size:19px;color:var(--white)}
.header .social{left:716px;top:177px}
.s-qx{background:#3b5998!important}.s-ch{background:#2aa3de!important}.s-vl{background:#c4302b!important}.s-sb{background:#cb2027!important}.s-zt{background:#dd4b39!important}
.search{left:562px;top:237px;width:454px;height:34px;display:flex;background:var(--white)}
.search span{flex:1;font-size:11px;color:#999;padding:11px 16px}
.search b{width:64px;background:#1a8fd6;display:flex;align-items:center;justify-content:center}

/* nav */
.nav{left:0;top:287px;width:1046px;height:59px;background:linear-gradient(var(--nav-top),var(--nav-bot));display:flex;list-style:none}
.nav li{color:var(--white);font-family:"Roboto Condensed",sans-serif;font-size:18px;padding:0 26px;display:flex;align-items:center;border-right:1px solid #15151b}
.nav li.active{color:#4aa3e0;background:#3a3a46}
.dropdown{left:88px;top:347px;width:251px;list-style:none;background:#4e4e58}
.dropdown li{height:39px;display:flex;align-items:center;gap:14px;padding-left:10px;color:var(--white);font-size:12px;font-weight:700;border-bottom:1px solid #3a3a42}
.dropdown li.on{background:var(--menu-blue)}
.dropdown i{width:16px;height:16px;border:1.5px solid #ddd;border-radius:50%}

/* slider */
.slider{left:0;top:346px;width:1046px;height:422px;background:linear-gradient(#47b0b4 0%,#8fcfbf 65%,#67b84a 85%,#4fa13b 100%);z-index:0}
.slider-arrow{top:189px;width:40px;height:40px}
.dropdown{z-index:2}

/* main */
.overview{left:25px;top:803px;width:640px;font-size:32px;font-weight:500;line-height:42px;color:#111}
.motd{left:91px;top:994px;width:481px;height:134px;background:var(--muted);border-radius:8px;text-align:center;color:var(--green)}
.motd h3{font-style:italic;font-weight:500;font-size:25px;margin-top:14px}
.motd p{font-style:italic;font-size:14px;line-height:21px;margin-top:10px}
.join{left:674px;top:804px;width:342px;height:324px;background:var(--panel);border:1px solid var(--panel-line);border-radius:3px}
.join h3{text-align:center;color:var(--green);font-size:22px;font-weight:700;margin-top:12px}
.field{position:absolute;left:21px;width:301px;height:46px;background:#e4e4e4;border:1px solid #c9c9c9;display:flex;align-items:center;gap:14px;padding-left:16px;color:#777;font-size:16px}
.field i{width:22px;height:16px;background:#bcbcbc;border-radius:2px}
.btn{position:absolute;left:21px;width:301px;background:linear-gradient(#2a9a58,var(--green-dark));color:var(--white);display:flex;align-items:center;border-radius:2px}
.btn svg{position:absolute;left:8px}
.btn.login{top:173px;height:58px;justify-content:center;font-size:25px;font-weight:700}
.btn.create{top:242px;height:56px;font-size:24px;padding-left:46px}

.blog{left:26px;top:1150px;width:624px;height:294px;background:var(--panel);border:1px solid var(--panel-line)}
.panel-title{color:var(--green);font-size:24px;font-weight:700}
.blog .panel-title{position:absolute;left:12px;top:12px}
.post{position:absolute;top:63px;width:196px}
.post .thumb{width:104px;height:104px;border-radius:50%;margin-left:44px;background:linear-gradient(#9cc6e6,#6f8ea8 60%,#4e6172);border:3px solid #ddd}
.post h4{font-style:italic;font-weight:700;font-size:15px;color:var(--green);margin-top:10px}
.post p{font-size:10.5px;line-height:13.5px;margin-top:3px;color:#222}
.post a{display:block;text-align:right;font-size:11px;font-style:italic;color:var(--link-blue);margin-top:8px;text-decoration:none}

.upcoming{left:674px;top:1150px;width:342px;height:294px;background:var(--panel);border:1px solid var(--panel-line)}
.upcoming .panel-title{text-align:center;margin-top:10px}
.auction{position:absolute;left:5px;display:flex;gap:12px;width:330px}
.auction b{flex:none;width:32px;height:32px;border-radius:50%;background:var(--green);color:var(--white);font-size:20px;display:flex;align-items:center;justify-content:center;margin-top:9px}
.auction p{font-size:11.5px;line-height:19px;color:var(--link-blue)}
.view-all{position:absolute;left:254px;top:260px;width:70px;height:24px;background:var(--green);color:var(--white);font-size:11px;font-weight:700;border-radius:5px;display:flex;align-items:center;justify-content:center}

/* testimonials */
.testimonials{left:0;top:1464px;width:1046px;height:300px;background:var(--quote-bg);color:var(--white)}
.testimonials h2{position:absolute;left:26px;top:30px;font-size:25px;font-weight:500}
.quote{position:absolute;top:83px;width:500px}
.quote .avatar{position:absolute;left:0;top:18px;width:110px;height:110px;border-radius:50%;background:radial-gradient(#f0f0f0,#b9c6cf);border:3px solid #eee}
.quote p{margin-left:133px;font-style:italic;font-size:15.5px;line-height:24px}
.quote cite{display:block;text-align:right;font-size:12.5px;margin-top:14px;padding-right:48px}
.dots{position:absolute;left:491px;top:283px;display:flex;gap:13px;transform:translateY(-20px)}
.dots i{width:14px;height:14px;border-radius:50%;background:var(--white)}
.dots i.on{background:var(--green)}

/* footer */
.footer{left:0;top:1764px;width:1046px;height:363px;background:var(--footer-bg);color:var(--white)}
.footer .brand{left:25px;top:34px;width:433px;height:324px;border-width:14px}
.footer .brand-name{font-size:88px}
.copyright{left:478px;top:36px;font-size:13px;display:flex;gap:6px;align-items:center}
.badges{left:478px;top:68px;width:361px;height:72px;background:#cfcfcf;display:flex;align-items:center;justify-content:space-around}
.badges i{width:90px;height:44px;background:#1e1e1e}
.badges i.oval{border-radius:50%;width:96px}
.foot-contact{left:494px;top:164px;width:300px}
.foot-contact h3{font-size:20px;font-weight:500;padding-bottom:8px;border-bottom:1px solid #777}
.foot-contact ul{list-style:none;font-size:13px;line-height:25.5px;margin-top:8px}
.footer .social{left:882px;top:32px;gap:6px}
.footer .social li{width:24px;height:24px;font-size:11px}
.foot-links{left:876px;top:66px;list-style:none;font-size:13px;line-height:18.7px}
</style>
</head>
<body>
<div class="site">
  <header class="abs header">
    <div class="abs brand"><span class="brand-mark"></span><span class="brand-name">Harrow</span></div>
    <ul class="abs contact-list">
      <li><svg viewBox="0 0 14 14"><rect width="14" height="14" rx="2" fill="#ddd"/><path d="M7 3a3 3 0 0 0-3 3c0 2 3 5 3 5s3-3 3-5a3 3 0 0 0-3-3z" fill="#0e6b3a"/></svg>- 5127 Old Tenbury Lane, Scottsville, KY 42190</li>
      <li><svg viewBox="0 0 14 14"><rect width="14" height="14" rx="2" fill="#ddd"/><rect x="4" y="2" width="6" height="10" rx="1" fill="#0e6b3a"/></svg>- 270-555-0143</li>
      <li><svg viewBox="0 0 14 14"><rect x="1" y="5" width="12" height="7" rx="1" fill="#ddd"/><rect x="3" y="2" width="8" height="4" fill="#ddd"/></svg>- Fax: 270-555-0179</li>
      <li><svg viewBox="0 0 14 14"><rect y="2" width="14" height="10" rx="1" fill="#ddd"/><path d="M0 3l7 5 7-5" stroke="#0e6b3a" fill="none"/></svg>- info@harrowlandbidhouse.example</li>
    </ul>
    <div class="abs find-us"><span class="tag"></span>Find us on:</div>
    <ul class="abs social">
      <li class="s-qx" aria-label="QX">Q</li><li class="s-ch" aria-label="chirpo">C</li><li class="s-vl" aria-label="vidloop">V</li><li class="s-sb" aria-label="snapboard">S</li><li class="s-zt" aria-label="zentro+">Z</li>
    </ul>
    <div class="abs search"><span>Type what you want to search..</span><b><svg width="18" height="18" viewBox="0 0 18 18"><circle cx="7" cy="7" r="5" stroke="#fff" stroke-width="2.2" fill="none"/><path d="M11 11l5 5" stroke="#fff" stroke-width="2.4"/></svg></b></div>
  </header>

  <ul class="abs nav">
    <li>Home</li><li class="active">All Auctions&nbsp;<svg width="12" height="8" viewBox="0 0 12 8"><path d="M1 1l5 5 5-5" stroke="#fff" stroke-width="2" fill="none"/></svg></li><li>Real Estate for Sale</li><li>Services</li><li>About Us</li><li>Contact Us</li>
  </ul>

  <div class="abs slider" role="img" aria-label="Illustrated city skyline with towers over a green hill">
    <svg class="abs slider-arrow" style="left:23px" viewBox="0 0 40 40"><circle cx="20" cy="20" r="17" stroke="#fff" stroke-width="3" fill="none"/><path d="M23 12l-9 8 9 8z" fill="#fff"/></svg>
    <svg class="abs slider-arrow" style="left:981px" viewBox="0 0 40 40"><circle cx="20" cy="20" r="17" stroke="#fff" stroke-width="3" fill="none"/><path d="M17 12l9 8-9 8z" fill="#fff"/></svg>
  </div>

  <ul class="abs dropdown">
    <li><i></i>Up Comming Auctions</li><li class="on"><i></i>Online Auctions</li><li><i></i>Past Auctions</li>
  </ul>

  <h1 class="abs overview">Company Overview Company Overview Company Overview Company Overview Company Overview Company Overview Company Overview Company Overview</h1>

  <section class="abs motd">
    <h3>Message of the day</h3>
    <p>Lorem ipsum dolor sit amet, consectetur adipiscing elit. Curabitur<br>Lorem ipsum dolor sit amet, consectetur adipiscing elit. Curabitur<br>Lorem ipsum dolor sit amet, consectetur adipiscing elit. Curabitur</p>
  </section>

  <section class="abs join">
    <h3>Join Harrow</h3>
    <div class="field" style="top:62px"><i></i>Email</div>
    <div class="field" style="top:111px"><i style="width:16px;height:20px"></i>Password</div>
    <div class="btn login"><svg width="30" height="30" viewBox="0 0 30 30"><circle cx="15" cy="15" r="12" stroke="#fff" stroke-width="2" fill="none"/><path d="M12 9l7 6-7 6z" fill="#fff"/></svg>Login</div>
    <div class="btn create"><svg width="28" height="28" viewBox="0 0 28 28"><circle cx="14" cy="14" r="11" stroke="#fff" stroke-width="2" fill="none"/><path d="M14 8v12M8 14h12" stroke="#fff" stroke-width="2"/></svg>Create New Account</div>
  </section>

  <section class="abs blog">
    <h2 class="panel-title">Recent Blog Posts</h2>
    <article class="post" style="left:8px"><div class="thumb" role="img" aria-label="City towers photo"></div><h4>Latest News &amp; Events 01</h4><p>Lorem ipsum dolor sit amet<br>Lorem ipsum dolor sit amet, consectet<br>Lorem ipsum dolor sit amet, consectet<br>Lorem ipsum dolor sit amet, consectet</p><a href="#">Continue ... ...</a></article>
    <article class="post" style="left:216px"><div class="thumb" role="img" aria-label="City towers photo"></div><h4>Latest News &amp; Events 01</h4><p>Lorem ipsum dolor sit amet, consectet<br>Lorem ipsum dolor sit amet,<br>Lorem ipsum dolor sit amet, consectet<br>Lorem ipsum dolor sit amet, consectet</p><a href="#">Continue ... ...</a></article>
    <article class="post" style="left:415px"><div class="thumb" role="img" aria-label="City towers photo"></div><h4>Latest News &amp; Events 01</h4><p>Lorem ipsum dolor sit amet, consectet<br>Lorem ipsum dolor sit amet, consectet<br>Lorem ipsum dolor sit amet,<br>Lorem ipsum dolor sit amet, consectet</p><a href="#">Continue ... ...</a></article>
  </section>

  <section class="abs upcoming">
    <h2 class="panel-title">Upcomming Auctions</h2>
    <div class="auction" style="top:56px"><b>1</b><p>Lorem ipsum dolor sit amet, consectetur adipiscing<br>Lorem ipsum dolor sit amet, consectetur adipiscing<br>Lorem ipsum dolor sit amet.</p></div>
    <div class="auction" style="top:122px"><b>2</b><p>Lorem ipsum dolor sit amet, consectetur adipiscing<br>Lorem ipsum dolor sit amet, consectetur adipiscing<br>Lorem ipsum dolor sit amet, consectetur.</p></div>
    <div class="auction" style="top:195px"><b>3</b><p>Lorem ipsum dolor sit amet, consectetur adipiscing<br>Lorem ipsum dolor sit amet, consectetur adipiscing<br>Lorem ipsum dolor.</p></div>
    <div class="view-all">View All</div>
  </section>

  <section class="abs testimonials">
    <h2>What Client's Say</h2>
    <blockquote class="quote" style="left:26px"><div class="avatar" role="img" aria-label="Portrait photo of a client"></div><p>Lorem ipsum dolor sit amet, consectetur adipiscing elit. Curabitur non bibendum leo. Ut blandit in leo sit amet. Nibh tellus efficitur magna, at blandit nibh ligula eu mi. Suspendisse fermentum, nisl eget accumsan posuere.</p><cite>Delia, Box Hill, VIC</cite></blockquote>
    <blockquote class="quote" style="left:537px"><div class="avatar" role="img" aria-label="Portrait photo of a client"></div><p>Lorem ipsum dolor sit amet, consectetur adipiscing elit. Curabitur non bibendum leo. Ut blandit in leo sit amet. Nibh tellus efficitur magna, at blandit nibh ligula eu mi. Suspendisse fermentum, nisl eget accumsan posuere.</p><cite>Owen, Liverpool, NSW</cite></blockquote>
    <div class="dots"><i></i><i></i><i class="on"></i><i></i><i></i></div>
  </section>

  <footer class="abs footer">
    <div class="abs brand"><span class="brand-mark"></span><span class="brand-name">Harrow</span></div>
    <div class="abs copyright"><svg width="12" height="12" viewBox="0 0 12 12"><circle cx="6" cy="6" r="5" stroke="#fff" fill="none"/></svg>All Rights Reserved 2015</div>
    <div class="abs badges" role="img" aria-label="Association membership badges"><i></i><i class="oval"></i><i></i></div>
    <div class="abs foot-contact">
      <h3>Contact Us</h3>
      <ul><li>- 5127 Old Tenbury Lane, Scottsville, KY 42190</li><li>- 270-555-0143</li><li>- Fax: 270-555-0179</li><li>- Email:info@harrowlandbidhouse.example</li></ul>
    </div>
    <ul class="abs social">
      <li class="s-qx" aria-label="QX">Q</li><li class="s-ch" aria-label="chirpo">C</li><li class="s-vl" aria-label="vidloop">V</li><li class="s-sb" aria-label="snapboard">S</li><li class="s-zt" aria-label="zentro+">Z</li>
    </ul>
    <ul class="abs foot-links"><li>Home</li><li>All Auctions</li><li>Real Estate for Sale</li><li>Services</li><li>About Us</li><li>Privacy Policy</li><li>Join Now</li></ul>
  </footer>
</div>
</body>
</html>
```